tobrin family medicine business cards

create business cards for 7 family medicine providers and 4 admin using attached logo
2 locations
appointment reminder on back of cards
will provide more info regarding names,addresses, credentials etc once started

```html
<!DOCTYPE html>
<html lang="en">
<head>
<meta charset="utf-8">
<title>Tobrin Family Medicine – Business Cards</title>
<link rel="stylesheet" href="https://fonts.googleapis.com/css2?family=Cinzel:wght@500;600&family=Poppins:wght@400;500&display=swap">
<style>
  :root {
    --navy: #27215f;
    --sky: #2aa3dc;
    --ink: #1f1d3d;
    --card: #ffffff;
    --backdrop: #e6e6ea;
    --rule: #9a9aa6;
  }
  * { box-sizing: border-box; margin: 0; padding: 0; }
  html, body { width: 1200px; height: 880px; overflow: hidden; }
  body {
    background: var(--backdrop);
    position: relative;
    font-family: "Poppins", sans-serif;
    color: var(--navy);
  }
  .card {
    position: absolute;
    width: 700px;
    height: 400px;
    background: var(--card);
    border-radius: 26px;
    box-shadow: 0 10px 28px rgba(0,0,0,.18);
    overflow: hidden;
  }
  .card--front { left: 110px; top: 30px; }
  .card--back  { left: 390px; top: 450px; }

  /* brand name placeholder: plain text, one colour, one weight */
  .brand {
    position: absolute;
    text-align: center;
    font-family: "Poppins", sans-serif;
    font-weight: 500;
    font-size: 24px;
    line-height: 1.25;
    color: var(--navy);
  }
  .brand__dot { width: 56px; height: 56px; border-radius: 50%; background: var(--sky); margin: 0 auto 12px; }

  .card--front .brand { left: 26px; top: 60px; width: 240px; }
  .divider { position: absolute; left: 282px; top: 52px; width: 1px; height: 150px; background: var(--navy); }

  .providers { position: absolute; left: 300px; top: 44px; }
  .providers__lead { font-family: "Cinzel", serif; font-weight: 600; font-size: 24px; color: var(--navy); margin-bottom: 6px; }
  .providers__list { list-style: none; font-size: 12.5px; line-height: 1.42; color: var(--navy); }

  .accent-line { position: absolute; left: 42px; top: 222px; width: 620px; height: 2px; background: var(--sky); }

  .location { position: absolute; font-size: 14px; line-height: 1.35; color: var(--ink); }
  .location--primary { left: 54px; top: 254px; }
  .location--secondary { left: 410px; top: 240px; }
  .location__row { display: flex; align-items: center; gap: 8px; }
  .location__row svg { width: 12px; height: 12px; flex: none; }
  .location__addr { margin-bottom: 4px; }

  /* back */
  .card--back .brand { left: 70px; top: 170px; width: 260px; }
  .appointment { position: absolute; left: 330px; top: 46px; width: 340px; }
  .appointment__title { font-family: "Cinzel", serif; font-weight: 500; font-size: 24px; letter-spacing: 2px; color: var(--navy); margin-bottom: 22px; }
  .field-row { display: flex; align-items: flex-end; gap: 8px; height: 34px; font-size: 15px; color: var(--navy); }
  .field-row__line { flex: 1; border-bottom: 1px solid var(--rule); height: 18px; }
  .blank-line { border-bottom: 1px solid var(--rule); height: 34px; }
</style>
</head>
<body>

<section class="card card--front">
  <div class="brand">
    <div class="brand__dot"></div>
    <div class="brand__name">Tobrin<br>Family Medicine</div>
  </div>
  <div class="divider"></div>
  <div class="providers">
    <h1 class="providers__lead">Dr. Alan Tobrin, D.O., P.A.</h1>
    <ul class="providers__list">
      <li>Board Certified Family Medicine</li>
      <li>Dr. Marian Tobrin, DNP | Dr. Joan Pellet, DNP</li>
      <li>Renee Dalvo, APRN</li>
      <li>Dr. Olivia Marsten, DNP</li>
      <li>Dana Whitcombe, MSN, APRN-BC</li>
      <li>Dr. Lena Corvasi, MD</li>
    </ul>
  </div>
  <div class="accent-line"></div>

  <div class="location location--primary">
    <div class="location__addr">4410 Harlow Rd. #220<br>Brookvale, FL 33390</div>
    <div class="location__row"><svg viewBox="0 0 12 12"><path d="M3 1l2 2.5-1.2 1.3c.6 1.3 1.7 2.4 3 3L8 6.6 10.5 8.5 9.5 11C5 11 1 7 1 2.5z" fill="var(--sky)"/></svg>555-014-7660</div>
    <div class="location__row"><svg viewBox="0 0 12 12"><rect x="3" y="1" width="6" height="3" fill="var(--sky)"/><rect x="1" y="4" width="10" height="5" rx="1" fill="var(--sky)"/><rect x="3" y="8" width="6" height="3" fill="#fff" stroke="var(--sky)"/></svg>555-014-2075</div>
    <div class="location__row"><svg viewBox="0 0 12 12"><rect x="1" y="2.5" width="10" height="7" fill="var(--sky)"/><path d="M1 2.5l5 4 5-4" fill="none" stroke="#fff"/></svg>office@tobrinclinic.com</div>
  </div>

  <div class="location location--secondary">
    <div class="location__addr">1800 N. Meridian Pkwy #201<br>Fairhaven, FL 33392</div>
    <div class="location__row"><svg viewBox="0 0 12 12"><path d="M3 1l2 2.5-1.2 1.3c.6 1.3 1.7 2.4 3 3L8 6.6 10.5 8.5 9.5 11C5 11 1 7 1 2.5z" fill="var(--sky)"/></svg>555-017-9908</div>
    <div class="location__row"><svg viewBox="0 0 12 12"><rect x="3" y="1" width="6" height="3" fill="var(--sky)"/><rect x="1" y="4" width="10" height="5" rx="1" fill="var(--sky)"/><rect x="3" y="8" width="6" height="3" fill="#fff" stroke="var(--sky)"/></svg>555-017-2728</div>
    <div class="location__row"><svg viewBox="0 0 12 12"><circle cx="6" cy="6" r="5" fill="var(--sky)"/><path d="M1 6h10M6 1c-2.5 3-2.5 7 0 10M6 1c2.5 3 2.5 7 0 10" fill="none" stroke="#fff" stroke-width=".8"/></svg>www.TobrinClinic.com</div>
  </div>
</section>

<section class="card card--back">
  <div class="appointment">
    <h2 class="appointment__title">APPOINTMENT</h2>
    <div class="field-row"><span>Name</span><span class="field-row__line"></span></div>
    <div class="field-row"><span>Date</span><span class="field-row__line"></span><span>Time</span><span class="field-row__line"></span></div>
    <div class="blank-line"></div>
    <div class="blank-line"></div>
    <div class="blank-line"></div>
  </div>
  <div class="brand">
    <div class="brand__dot"></div>
    <div class="brand__name">Tobrin<br>Family Medicine</div>
  </div>
</section>

</body>
</html>
```